Brightleaf Card Venture Flyer

I need a DL sized flyer that will be sent out to participants in our Brightleaf Card Venture - sharing 1million Brightleaf Cards with the world. This flyer will form the first tangible item most of our community will receive from Lifting the Horizon, so it needs to be able to communicate our goal of inspiring change, possibility, kindness and love in the world.

Target Market(s)

Women aged 30 - 50, sophisticated, generous, philanthropy minded, contemporary, elegant

Font styles to use
Sans Serif
Other font styles liked:
• Raleway

Colors

Designer to choose colors to be used in the design.

Requirements
Must have
• Must be DL size - i.e. one third of an A4. On one side the flyer must also include space for the Brightleaf Cards to be stuck - the brightleaf cards are Stikkas that are 3in (76mm) square.
• The logo must be included somewhere, along with the website and social media icons - liftingthehorizon.com.au, Facebook, Instagram, Twitter all @liftingthehorizon.
• The copy for the flyer is:
• Thank you so much for helping us to reach our goal of having one million brightleaf cards out in the world. Share one of our notes with a friend, a family member, with a total stranger, or perhaps just with yourself. And remember that you might just be Lifting the Horizon in someone else's day.
• Share the story of your brightleaf cards on social media with the hashtag #brightleafcardventure or send us a photo and your story to bcventure@liftingthehorizon.com.au

```html
<!DOCTYPE html>
<html lang="en">
<head>
<meta charset="utf-8">
<title>Brightleaf Card Venture – DL Flyer</title>
<link rel="stylesheet" href="https://fonts.googleapis.com/css2?family=Open+Sans:wght@400;600;700&family=Montserrat:wght@700;800&display=swap">
<style>
  :root {
    --teal-deep: #0b5a4f;
    --teal-mid: #1f7a6d;
    --teal-light: #2e8f80;
    --teal-text: #1b6f62;
    --paper: #f3f3f3;
    --mist-light: #eeeeee;
    --mist-dark: #8d8d8d;
    --stage: #e9e6e1;
    --white: #ffffff;
  }
  * { box-sizing: border-box; margin: 0; padding: 0; }
  html, body { width: 1200px; height: 844px; overflow: hidden; }
  body {
    background: var(--stage);
    font-family: "Open Sans", Arial, sans-serif;
    position: relative;
  }
  .flyer {
    position: absolute;
    top: 42px;
    width: 358px;
    height: 760px;
    overflow: hidden;
    box-shadow: 0 2px 6px rgba(0,0,0,0.12);
  }
  .flyer--front { left: 222px; background: var(--paper); }
  .flyer--back {
    left: 620px;
    background: linear-gradient(180deg, var(--teal-light) 0%, var(--teal-mid) 40%, var(--teal-deep) 100%);
    color: var(--white);
  }

  /* Front */
  .hero {
    position: absolute;
    inset: 0 0 auto 0;
    height: 430px;
    background:
      radial-gradient(ellipse at 50% 78%, var(--mist-dark) 0%, #b8b8b8 30%, transparent 62%),
      linear-gradient(180deg, #d2d2d2 0%, var(--mist-light) 45%, #cfcfcf 75%, var(--paper) 100%);
  }
  .brand-name {
    position: absolute;
    top: 92px;
    left: 0; right: 0;
    text-align: center;
    font-family: "Open Sans", Arial, sans-serif;
    font-weight: 600;
    font-size: 27px;
    color: var(--teal-text);
  }
  .brand-dot {
    display: block;
    width: 14px; height: 14px;
    margin: 0 auto 12px;
    border-radius: 50%;
    background: var(--teal-text);
  }
  .thanks {
    position: absolute;
    top: 462px;
    left: 34px; right: 34px;
    font-size: 14.5px;
    line-height: 1.5;
    text-align: justify;
    color: var(--teal-text);
  }
  .web-band {
    position: absolute;
    left: 0; right: 0; bottom: 0;
    height: 64px;
    background: var(--teal-deep);
    color: var(--white);
    font-weight: 700;
    font-size: 15px;
    display: flex; align-items: center; justify-content: center;
  }

  /* Back */
  .hashtag {
    position: absolute;
    top: 34px; left: 0; right: 0;
    text-align: center;
    font-family: "Montserrat", Arial, sans-serif;
    font-weight: 800;
    font-size: 19px;
    letter-spacing: 0.3px;
  }
  .sticker-space {
    position: absolute;
    top: 84px;
    left: 41px;
    width: 276px;
    height: 276px;
    background: var(--paper);
  }
  .share-copy {
    position: absolute;
    top: 410px; left: 26px; right: 26px;
    text-align: center;
    font-size: 14px;
    line-height: 1.55;
  }
  .share-copy strong { font-weight: 700; }
  .social {
    position: absolute;
    bottom: 58px; left: 0; right: 0;
    text-align: center;
  }
  .social-dot {
    display: block;
    width: 34px; height: 34px;
    margin: 0 auto 10px;
    border-radius: 50%;
    background: var(--white);
  }
  .social-handle {
    font-family: "Montserrat", Arial, sans-serif;
    font-weight: 700;
    font-size: 15px;
  }
</style>
</head>
<body>
  <section class="flyer flyer--front">
    <div class="hero" role="img" aria-label="Black and white photograph of snow-capped mountains rising through mist"></div>
    <div class="brand-name"><span class="brand-dot"></span>Lifting the Horizon</div>
    <p class="thanks">Thank you so much for helping us to reach our goal of having one million brightleaf cards out in the world. Share one of our notes with a friend, a family member, with a total stranger, or perhaps just with yourself. And remember that you might just be Lifting the Horizon in someone else's day.</p>
    <div class="web-band">liftingthehorizon.com.au</div>
  </section>

  <section class="flyer flyer--back">
    <h1 class="hashtag">#brightleafcardventure</h1>
    <div class="sticker-space" aria-label="Space for a 76 mm Brightleaf Card"></div>
    <p class="share-copy">Share the story of your brightleaf cards on social media with the hashtag <strong>#brightleafcardventure</strong> or send us a photo and your story to bcventure@liftingthehorizon.com.au</p>
    <div class="social">
      <span class="social-dot"></span>
      <span class="social-handle">@liftingthehorizon</span>
    </div>
  </section>
</body>
</html>
```